2021 Personalized Vision Poster

A beautiful, pleasing design for my 2021 vision poster. Looking probably for an infographic. Open to shortening the wording used if able. As you will notice, each color represents a different category. Let me know if you need more details. The title of each section are mostly listed, but starting with the upper left with “my primary question” going counter-clockwise: my primary question, away values and rules, life purpose, power values (red), toward values and rules, top 4 goals for 2021 (middle), and relationship vision (middle). Basically, I’m just looking for a nice font and different formatting for my words.

Requirements
Must have
• All of the sections with a majority of the words used.
Nice to have
• Infographic would be nice, if possible. More concerned with a beautiful layout of words already expressed.
Should not have
• A complete reworking of the words used.

```html
<!DOCTYPE html>
<html lang="en">
<head>
<meta charset="utf-8">
<title>2021 Live Courageously – Vision Poster</title>
<link rel="stylesheet" href="https://fonts.googleapis.com/css2?family=Bebas+Neue&family=Playfair+Display:ital,wght@0,400;0,700;0,800;1,700;1,800&family=Roboto:wght@400;500;700&display=swap">
<style>
:root{
  --navy:#1f3b66;
  --blue:#2a5088;
  --blue-dark:#223f6d;
  --sky:#1da1e6;
  --yellow:#f2b807;
  --yellow-dark:#d9a300;
  --gold:#d4a400;
  --gold-light:#f2cd45;
  --lime:#8ff03c;
  --lime-dark:#6fd11f;
  --black:#222222;
  --grey:#8f8f8f;
  --grey-dark:#6c6c6c;
  --panel:#ececec;
  --ink:#2b2b2b;
  --red:#d11f2a;
  --white:#ffffff;
  --check:#3f6fb0;
}
*{box-sizing:border-box;margin:0;padding:0}
html,body{width:1200px;height:848px;overflow:hidden;background:var(--white)}
.poster{position:relative;width:1200px;height:848px;background:var(--white);font-family:'Roboto',sans-serif;color:var(--ink);overflow:hidden}
.abs{position:absolute}

/* header */
.header{left:0;top:0;width:1200px;height:128px;background:var(--blue);overflow:hidden}
.header-shade{left:0;top:0;width:1200px;height:128px}
.title{left:0;top:8px;width:1200px;padding-left:98px;font-family:'Bebas Neue',sans-serif;font-size:112px;line-height:1;color:var(--white);letter-spacing:5px;white-space:nowrap}
.name-ribbon{left:-40px;top:30px;width:170px;height:34px;background:var(--lime);transform:rotate(-45deg);transform-origin:center;display:flex;align-items:center;justify-content:center}
.name-ribbon span{font-family:'Bebas Neue',sans-serif;font-size:22px;color:#1b2b1b;letter-spacing:1px;transform:translateY(-2px)}

/* primary question */
.question-box{left:40px;top:175px;width:335px;height:160px;border:1.5px dashed #6a6a6a;border-radius:4px}
.question-mark{left:318px;top:140px;font-family:'Playfair Display',serif;font-weight:800;font-size:190px;line-height:1;color:#c4c4c4}
.quote-mark{left:58px;top:152px;font-family:'Playfair Display',serif;font-weight:800;font-size:78px;line-height:1;color:#7fa0d2}
.question-text{left:60px;top:208px;width:300px;font-family:'Playfair Display',serif;font-size:19px;line-height:23px;color:var(--ink)}
.question-label{left:60px;top:282px;font-family:'Playfair Display',serif;font-weight:700;font-size:23px;color:var(--navy)}

/* value headings */
.value-bar{height:40px;border-radius:6px;display:flex;align-items:center;font-family:'Bebas Neue',sans-serif;font-size:28px;letter-spacing:.5px}
.value-bar.away{left:100px;top:376px;width:296px;background:var(--black);color:var(--yellow);padding-left:42px}
.value-bar.toward{left:870px;top:166px;width:294px;background:var(--blue-dark);color:#35b7ff;padding-left:38px}
.badge{border-radius:50%;display:flex;align-items:center;justify-content:center}
.badge.away{left:38px;top:352px;width:80px;height:80px;background:var(--white);border:2px solid var(--lime)}
.badge.away .core{width:66px;height:66px;border-radius:50%;background:var(--yellow);display:flex;align-items:center;justify-content:center}
.badge.toward{left:804px;top:146px;width:80px;height:80px;background:var(--white);border:2px solid var(--sky)}
.badge.toward .core{width:68px;height:68px;border-radius:50%;background:var(--sky);display:flex;align-items:center;justify-content:center}

.avoid-note{left:60px;top:418px;width:330px;text-align:center;font-size:14px;color:var(--ink)}
.check-list{list-style:none}
.check-list li{position:relative;padding-left:26px}
.check-list li svg{position:absolute;left:0;top:2px}
.away-list{left:66px;top:450px;width:330px;font-size:14.5px;line-height:25px}
.away-list li svg{top:5px}
.instead-bar{left:59px;top:536px;width:329px;height:40px;border-radius:6px 6px 0 0;background:linear-gradient(var(--blue),var(--navy));color:var(--yellow);font-family:'Bebas Neue',sans-serif;font-size:28px;display:flex;align-items:center;justify-content:center}
.instead-panel{left:59px;top:576px;width:329px;height:135px;background:var(--panel);border-radius:0 0 6px 6px}
.instead-list{left:72px;top:588px;width:292px;font-size:14px;line-height:18px}
.instead-list li{margin-bottom:4px}

/* centre column */
.centre-panel{left:416px;top:128px;width:351px;height:720px;background:linear-gradient(90deg,#efefe6,#fbfbf4 50%,#efefe6)}
.tile{width:154px;height:156px;border-radius:14px;overflow:hidden}
.tile .num{position:absolute;font-family:'Bebas Neue',sans-serif;font-size:96px;line-height:1}
.tile .label{position:absolute;width:100%;text-align:center;font-family:'Bebas Neue',sans-serif;font-size:38px;line-height:1}
.tile .ico{position:absolute;left:0;width:100%;display:flex;justify-content:center}
.tile.rental{left:431px;top:145px;background:var(--yellow)}
.tile.weight{left:594px;top:145px;background:var(--black)}
.tile.team{left:431px;top:310px;background:var(--lime)}
.tile.money{left:594px;top:310px;background:var(--grey)}
.top4{left:520px;top:238px;width:138px;height:138px;border-radius:50%;background:var(--navy);border:6px solid var(--white);display:flex;align-items:center;justify-content:center;font-family:'Bebas Neue',sans-serif;font-size:58px;color:var(--white)}

.relationship-bar{left:431px;top:495px;width:317px;height:45px;background:var(--navy);color:var(--lime);font-weight:700;font-size:25px;display:flex;align-items:center;justify-content:center;letter-spacing:.3px}
.rel-item{height:30px;display:flex;align-items:center;font-weight:500;font-size:22px;color:var(--ink)}
.rel-item .ico{width:26px;display:flex;justify-content:center;margin-right:8px}
.rel-item .word{height:30px;padding:0 8px;display:flex;align-items:center;background:linear-gradient(90deg,#e6e6e0,rgba(230,230,224,0))}

/* right column */
.toward-list{left:822px;top:241px;width:322px;font-size:16px;line-height:19px}
.toward-list li{padding-left:28px;margin-bottom:8.5px}
.toward-list li svg{top:1px}
.body-title{left:800px;top:504px;width:380px;text-align:center;font-family:'Playfair Display',serif;font-weight:800;font-size:31px;line-height:40px;color:var(--sky);white-space:nowrap}
.cycle{left:800px;top:560px;width:380px;height:160px}
.cycle-word{font-family:'Playfair Display',serif;font-weight:700;font-size:22px;color:var(--navy);transform:translate(-50%,-50%);white-space:nowrap}

/* footer */
.purpose{left:11px;top:731px;width:1168px;height:106px;background:linear-gradient(90deg,var(--gold) 0%,var(--gold-light) 50%,var(--gold) 100%);display:flex;align-items:center;justify-content:center;text-align:center}
.purpose p{font-family:'Playfair Display',serif;font-style:italic;font-weight:700;font-size:25px;line-height:38px;color:#1e1e1e}
</style>
</head>
<body>
<main class="poster">

  <header class="abs header">
    <svg class="abs header-shade" width="1200" height="128" viewBox="0 0 1200 128" aria-hidden="true">
      <polygon points="0,128 90,0 1130,0 1200,55 1200,128" fill="#254a80"/>
      <polygon points="70,128 160,40 1200,40 1200,128" fill="#1f3f70" opacity=".45"/>
    </svg>
    <div class="abs name-ribbon"><span>ALEX R.</span></div>
    <h1 class="abs title">2021- LIVE COURAGEOUSLY!</h1>
  </header>

  <!-- primary question -->
  <section>
    <div class="abs question-box"></div>
    <div class="abs question-mark">?</div>
    <div class="abs quote-mark">&ldquo;</div>
    <p class="abs question-text">How can I be even more grateful for the love in my heart for God myself and, and others?</p>
    <p class="abs question-label">- My Primary Question</p>
  </section>

  <!-- away values -->
  <section>
    <div class="abs value-bar away">AWAY VALUES AND RULES</div>
    <div class="abs badge away"><div class="core">
      <svg width="40" height="40" viewBox="0 0 40 40" aria-hidden="true">
        <path d="M4 30 q8-8 16-4 l8 0 q3 0 3 3 l-10 1 M4 30 l6 6 l14-2 l12-9 q1-4-3-3 l-8 5" fill="none" stroke="#1f1f1f" stroke-width="2.6" stroke-linejoin="round" stroke-linecap="round"/>
        <path d="M14 6v8M10 10h8M24 4v6M21 7h6M22 14v6M19 17h6" stroke="#1f1f1f" stroke-width="2.6" stroke-linecap="round"/>
      </svg>
    </div></div>
    <p class="abs avoid-note">ONLY IF I WERE TO AVOID...</p>
    <ul class="abs check-list away-list">
      <li><svg width="16" height="16" viewBox="0 0 16 16" aria-hidden="true"><circle cx="8" cy="8" r="6.5" fill="none" stroke="var(--check)" stroke-width="1.4"/><path d="M4.8 8.2l2.2 2.2 5.5-6" fill="none" stroke="var(--check)" stroke-width="1.6"/></svg>Consistent, unrighteous anger</li>
      <li><svg width="16" height="16" viewBox="0 0 16 16" aria-hidden="true"><circle cx="8" cy="8" r="6.5" fill="none" stroke="var(--check)" stroke-width="1.4"/><path d="M4.8 8.2l2.2 2.2 5.5-6" fill="none" stroke="var(--check)" stroke-width="1.6"/></svg>Consistent, debilitating, illusion of failure</li>
      <li><svg width="16" height="16" viewBox="0 0 16 16" aria-hidden="true"><circle cx="8" cy="8" r="6.5" fill="none" stroke="var(--check)" stroke-width="1.4"/><path d="M4.8 8.2l2.2 2.2 5.5-6" fill="none" stroke="var(--check)" stroke-width="1.6"/></svg>Consistent, debilitating anxiety</li>
    </ul>
    <div class="abs instead-bar">INSTEAD OF...</div>
    <div class="abs instead-panel"></div>
    <ul class="abs check-list instead-list">
      <li><svg width="16" height="16" viewBox="0 0 16 16" aria-hidden="true"><circle cx="8" cy="8" r="6.5" fill="none" stroke="var(--check)" stroke-width="1.4"/><path d="M4.8 8.2l2.2 2.2 5.5-6" fill="none" stroke="var(--check)" stroke-width="1.6"/></svg>Knowing that I alone have the power to choose to be angry</li>
      <li><svg width="16" height="16" viewBox="0 0 16 16" aria-hidden="true"><circle cx="8" cy="8" r="6.5" fill="none" stroke="var(--check)" stroke-width="1.4"/><path d="M4.8 8.2l2.2 2.2 5.5-6" fill="none" stroke="var(--check)" stroke-width="1.6"/></svg>Realizing God has made me<br>congueros-&nbsp; I will not fail</li>
      <li><svg width="16" height="16" viewBox="0 0 16 16" aria-hidden="true"><circle cx="8" cy="8" r="6.5" fill="none" stroke="var(--check)" stroke-width="1.4"/><path d="M4.8 8.2l2.2 2.2 5.5-6" fill="none" stroke="var(--check)" stroke-width="1.6"/></svg>Realizing Go has given me all the inner<br>peace I need</li>
    </ul>
  </section>

  <!-- top 4 goals -->
  <section>
    <div class="abs centre-panel"></div>

    <div class="abs tile rental">
      <span class="num" style="left:6px;top:95px;color:var(--yellow-dark)">1</span>
      <div class="ico" style="top:18px">
        <svg width="44" height="34" viewBox="0 0 44 34" aria-hidden="true"><path d="M22 2 L8 14 M22 2 L36 14" stroke="#1f1f1f" stroke-width="2"/><circle cx="22" cy="3" r="2.2" fill="#1f1f1f"/><rect x="4" y="14" width="36" height="18" fill="#1f1f1f"/><text x="22" y="28" text-anchor="middle" font-family="Roboto,sans-serif" font-weight="700" font-size="11" fill="#f2b807">RENT</text></svg>
      </div>
      <span class="label" style="top:62px;color:#1f1f1f">RENTAL</span>
    </div>

    <div class="abs tile weight">
      <span class="num" style="right:8px;top:95px;color:#111">2</span>
      <div class="ico" style="top:18px">
        <svg width="34" height="38" viewBox="0 0 34 38" aria-hidden="true"><circle cx="17" cy="6" r="3.5" fill="none" stroke="var(--yellow)" stroke-width="2.2"/><path d="M9 12 H25 L31 34 H3 Z" fill="none" stroke="var(--yellow)" stroke-width="2.6" stroke-linejoin="round"/></svg>
      </div>
      <span class="label" style="top:62px;color:var(--white)">175 LBS</span>
    </div>

    <div class="abs tile team">
      <span class="num" style="left:6px;top:95px;color:var(--lime-dark)">3</span>
      <div class="ico" style="top:48px">
        <svg width="52" height="38" viewBox="0 0 52 38" aria-hidden="true"><circle cx="12" cy="8" r="6" fill="#1f1f1f"/><circle cx="40" cy="8" r="6" fill="#1f1f1f"/><circle cx="26" cy="11" r="7.5" fill="#1f1f1f"/><path d="M2 28 q0-10 10-10 q6 0 8 4 H32 q2-4 8-4 q10 0 10 10Z" fill="#1f1f1f"/><path d="M12 37 q0-14 14-14 q14 0 14 14Z" fill="#1f1f1f"/></svg>
      </div>
      <span class="label" style="top:102px;color:#1f1f1f">TEAM</span>
    </div>

    <div class="abs tile money">
      <span class="num" style="left:4px;top:95px;color:var(--grey-dark)">4</span>
      <div class="ico" style="top:52px">
        <svg width="46" height="40" viewBox="0 0 46 40" aria-hidden="true"><g fill="#e9e9e9"><ellipse cx="16" cy="8" rx="13" ry="5"/><rect x="3" y="11" width="26" height="6" rx="3"/><rect x="3" y="19" width="26" height="6" rx="3"/><rect x="3" y="27" width="26" height="6" rx="3"/></g><circle cx="32" cy="24" r="11" fill="#e9e9e9" stroke="#8f8f8f" stroke-width="2"/><text x="32" y="29" text-anchor="middle" font-family="Roboto,sans-serif" font-weight="700" font-size="14" fill="#6c6c6c">$</text></svg>
      </div>
      <span class="label" style="top:102px;color:var(--white)">$250K</span>
    </div>

    <div class="abs top4">TOP 4</div>
  </section>

  <!-- relationship vision -->
  <section>
    <div class="abs relationship-bar">RELATIONSHIP VISION</div>

    <div class="abs rel-item" style="left:434px;top:565px"><span class="ico"><svg width="22" height="20" viewBox="0 0 22 20" aria-hidden="true"><path d="M11 19 L2 10 a5 5 0 0 1 9-6 a5 5 0 0 1 9 6Z" fill="var(--red)"/></svg></span><span class="word">LOVE</span></div>
    <div class="abs rel-item" style="left:434px;top:603px"><span class="ico"><svg width="26" height="20" viewBox="0 0 26 20" aria-hidden="true"><path d="M2 8 L8 3 L13 6 L18 3 L24 8 L15 17 Q13 19 11 17 Z M8 10 l5 5 M11 8 l5 5" fill="none" stroke="var(--red)" stroke-width="1.6" stroke-linejoin="round"/></svg></span><span class="word">RESPECT</span></div>
    <div class="abs rel-item" style="left:434px;top:642px"><span class="ico"><svg width="22" height="22" viewBox="0 0 22 22" aria-hidden="true"><circle cx="7" cy="4" r="2.5" fill="var(--red)"/><circle cx="15" cy="4" r="2.5" fill="var(--red)"/><path d="M3 20 V11 Q3 8 7 8 L11 12 L15 8 Q19 8 19 11 V20" fill="none" stroke="var(--red)" stroke-width="2"/></svg></span><span class="word">COURAGE</span></div>
    <div class="abs rel-item" style="left:434px;top:680px"><span class="ico"><svg width="24" height="22" viewBox="0 0 24 22" aria-hidden="true"><path d="M12 11 L7 6 a3 3 0 0 1 5-3 a3 3 0 0 1 5 3Z" fill="var(--red)"/><path d="M2 8 V16 L8 21 M22 8 V16 L16 21 M5 13 l5 4 M19 13 l-5 4" fill="none" stroke="var(--red)" stroke-width="1.8" stroke-linecap="round"/></svg></span><span class="word">DESIRE</span></div>

    <div class="abs rel-item" style="left:596px;top:565px"><span class="ico"><svg width="22" height="22" viewBox="0 0 22 22" aria-hidden="true"><circle cx="11" cy="11" r="9" fill="none" stroke="var(--red)" stroke-width="2"/></svg></span><span class="word">FUN</span></div>
    <div class="abs rel-item" style="left:596px;top:603px"><span class="ico"><svg width="22" height="22" viewBox="0 0 22 22" aria-hidden="true"><rect x="2" y="4" width="16" height="16" rx="4" fill="none" stroke="var(--red)" stroke-width="2"/><path d="M18 7 L15.5 4.5 a1.6 1.6 0 0 1 2.5-2 a1.6 1.6 0 0 1 2.5 2Z" fill="var(--red)"/></svg></span><span class="word">FLIRTY</span></div>
    <div class="abs rel-item" style="left:596px;top:642px"><span class="ico"><svg width="26" height="22" viewBox="0 0 26 22" aria-hidden="true"><path d="M9 19 L2 11 a4 4 0 0 1 7-5 a4 4 0 0 1 7 5Z M17 20 L11 13 a3.6 3.6 0 0 1 6-4.5 a3.6 3.6 0 0 1 6 4.5Z" fill="none" stroke="var(--red)" stroke-width="1.6"/></svg></span><span class="word">ROMANTIC</span></div>
  </section>

  <!-- toward values -->
  <section>
    <div class="abs value-bar toward">AWAY VALUES AND RULES</div>
    <div class="abs badge toward"><div class="core">
      <svg width="42" height="42" viewBox="0 0 40 40" aria-hidden="true">
        <path d="M4 30 q8-8 16-4 l8 0 q3 0 3 3 l-10 1 M4 30 l6 6 l14-2 l12-9 q1-4-3-3 l-8 5" fill="none" stroke="#fff" stroke-width="2.6" stroke-linejoin="round" stroke-linecap="round"/>
        <path d="M14 6v8M10 10h8M24 4v6M21 7h6M22 14v6M19 17h6" stroke="#fff" stroke-width="2.6" stroke-linecap="round"/>
      </svg>
    </div></div>
    <ul class="abs check-list toward-list">
      <li><svg width="17" height="17" viewBox="0 0 16 16" aria-hidden="true"><circle cx="8" cy="8" r="6.5" fill="none" stroke="var(--check)" stroke-width="1.4"/><path d="M4.8 8.2l2.2 2.2 5.5-6" fill="none" stroke="var(--check)" stroke-width="1.6"/></svg>GIving of myself and serve others, OR</li>
      <li><svg width="17" height="17" viewBox="0 0 16 16" aria-hidden="true"><circle cx="8" cy="8" r="6.5" fill="none" stroke="var(--check)" stroke-width="1.4"/><path d="M4.8 8.2l2.2 2.2 5.5-6" fill="none" stroke="var(--check)" stroke-width="1.6"/></svg>Accepting love from God or others, OR</li>
      <li><svg width="17" height="17" viewBox="0 0 16 16" aria-hidden="true"><circle cx="8" cy="8" r="6.5" fill="none" stroke="var(--check)" stroke-width="1.4"/><path d="M4.8 8.2l2.2 2.2 5.5-6" fill="none" stroke="var(--check)" stroke-width="1.6"/></svg>Allowing myself to stay present, OR</li>
      <li><svg width="17" height="17" viewBox="0 0 16 16" aria-hidden="true"><circle cx="8" cy="8" r="6.5" fill="none" stroke="var(--check)" stroke-width="1.4"/><path d="M4.8 8.2l2.2 2.2 5.5-6" fill="none" stroke="var(--check)" stroke-width="1.6"/></svg>Doing something ever when scary, OR</li>
      <li><svg width="17" height="17" viewBox="0 0 16 16" aria-hidden="true"><circle cx="8" cy="8" r="6.5" fill="none" stroke="var(--check)" stroke-width="1.4"/><path d="M4.8 8.2l2.2 2.2 5.5-6" fill="none" stroke="var(--check)" stroke-width="1.6"/></svg>Choosing to put myself first, OR</li>
      <li><svg width="17" height="17" viewBox="0 0 16 16" aria-hidden="true"><circle cx="8" cy="8" r="6.5" fill="none" stroke="var(--check)" stroke-width="1.4"/><path d="M4.8 8.2l2.2 2.2 5.5-6" fill="none" stroke="var(--check)" stroke-width="1.6"/></svg>Protecting vulnerability, OR</li>
      <li><svg width="17" height="17" viewBox="0 0 16 16" aria-hidden="true"><circle cx="8" cy="8" r="6.5" fill="none" stroke="var(--check)" stroke-width="1.4"/><path d="M4.8 8.2l2.2 2.2 5.5-6" fill="none" stroke="var(--check)" stroke-width="1.6"/></svg>Taking actions consistent with my<br>identity, OR</li>
      <li><svg width="17" height="17" viewBox="0 0 16 16" aria-hidden="true"><circle cx="8" cy="8" r="6.5" fill="none" stroke="var(--check)" stroke-width="1.4"/><path d="M4.8 8.2l2.2 2.2 5.5-6" fill="none" stroke="var(--check)" stroke-width="1.6"/></svg>Getting outdoor, OR</li>
      <li><svg width="17" height="17" viewBox="0 0 16 16" aria-hidden="true"><circle cx="8" cy="8" r="6.5" fill="none" stroke="var(--check)" stroke-width="1.4"/><path d="M4.8 8.2l2.2 2.2 5.5-6" fill="none" stroke="var(--check)" stroke-width="1.6"/></svg>Going or a little bit adventure, OR</li>
    </ul>
  </section>

  <!-- power values cycle -->
  <section>
    <h2 class="abs body-title">MOVING MY BODY!</h2>
    <svg class="abs cycle" width="380" height="160" viewBox="0 0 380 160" aria-hidden="true">
      <defs><marker id="arrowhead" markerWidth="8" markerHeight="8" refX="5" refY="4" orient="auto"><path d="M0 0 L6 4 L0 8" fill="none" stroke="#9aa6b8" stroke-width="1.3"/></marker></defs>
      <g fill="none" stroke="#9aa6b8" stroke-width="1.3" marker-end="url(#arrowhead)">
        <path d="M144 43 Q110 46 93 63"/>
        <path d="M287 58 Q275 40 255 38"/>
        <path d="M54 90 Q70 115 103 122"/>
        <path d="M146 141 Q166 137 185 141"/>
        <path d="M305 117 Q300 135 278 148"/>
      </g>
      <path d="M63 26 L55 42 H62 L57 56 L70 37 H63 L68 26Z" fill="var(--yellow)"/>
      <path d="M336 44 L329 37 a4 4 0 0 1 7-5 a4 4 0 0 1 7 5Z" fill="none" stroke="var(--yellow)" stroke-width="1.6"/>
    </svg>
    <span class="abs cycle-word" style="left:986px;top:598px">Courage</span>
    <span class="abs cycle-word" style="left:850px;top:633px">Power</span>
    <span class="abs cycle-word" style="left:1136px;top:628px">Love</span>
    <span class="abs cycle-word" style="left:920px;top:696px">Joy</span>
    <span class="abs cycle-word" style="left:1059px;top:700px">Presence</span>
  </section>

  <!-- life purpose -->
  <footer class="abs purpose">
    <p>The purpose of my life is to be loving, courageous, and fun! I seek adventure,<br>laugh and play, and live in God's identity for me</p>
  </footer>

</main>
</body>
</html>
```